European Indian Investment firm

I would like to have a complete make-over of an existing website. Have a look at : www.velmoranpartners-example.com
We are a European/Indian based investment firm that acquires stakes in European (Manufacturing) companies (industrial) and help them grow in India. We have a team in Europe (Barcelona, Zurich, Amsterdam) and in India (Bangalore).
Amongst the new lay-out of the website also the name and the logo of the site will change. I will upload the new company logo. The new site should broadly send out the same message which is bridging Europe and India and also it should have an industrial/manufacturing look. The wording and the various pages of the website will be broadly the same as the old one with some changes which we will provide further down the road. I

Target Market(s)

Europe and India. Entrepreneurs, CEO's and investors.

Industry/Entity Type

Investment

Coding

Coded - Design and coding required

Number of Pages Required

5+ page

Font styles to use
Sans Serif

Requirements
Must have
• site should have an industrial look and also it should reflect the bridging between the two continents Europe and India provided by the team helping companies to grow.

```html
<!DOCTYPE html>
<html lang="en">
<head>
<meta charset="utf-8">
<title>Velmoran Partners</title>
<link href="https://fonts.googleapis.com/css2?family=Open+Sans:wght@400;600;700&display=swap" rel="stylesheet">
<style>
:root{
  --teal:#1f6470;
  --teal-dark:#164b55;
  --tan:#b8a07a;
  --ink:#3a3a3a;
  --muted:#8a8a8a;
  --line:#e3e3e3;
  --footer:#2b2b2b;
  --footer-text:#9a9a9a;
  --paper:#ffffff;
}
*{box-sizing:border-box;margin:0;padding:0}
html,body{width:880px;height:1200px;overflow:hidden}
body{font-family:"Open Sans",Arial,sans-serif;color:var(--ink);background:var(--paper);position:relative}
.wrap{position:absolute;left:73px;width:734px}

/* header */
.brand{position:absolute;left:88px;top:22px;display:flex;align-items:center;gap:10px}
.brand-mark{width:34px;height:34px;background:var(--teal)}
.brand-name{font-size:22px;font-weight:700;color:var(--teal);letter-spacing:.5px}
.search{position:absolute;left:630px;top:36px;width:166px;height:24px;border:1px solid var(--line);font-size:10px;color:#aaa;padding:5px 8px;display:flex;justify-content:space-between;align-items:center}
.search svg{width:11px;height:11px}

.nav{top:97px;height:38px;background:var(--teal-dark);display:flex}
.nav a{flex:1;display:flex;align-items:center;justify-content:center;color:#fff;font-size:10px;font-weight:600;letter-spacing:.5px;text-decoration:none;border-right:1px solid rgba(255,255,255,.08)}
.nav a.active{background:var(--tan)}

/* hero */
.hero{top:135px;height:335px;background:linear-gradient(180deg,#cfe0ea 0%,#9fb9c9 55%,#5f7888 100%)}
.hero-welcome{position:absolute;left:9px;top:123px;width:240px;background:rgba(22,75,85,.92);color:#fff;padding:10px 12px}
.hero-welcome h1{font-size:12px;font-weight:700;letter-spacing:.4px;margin-bottom:5px}
.hero-welcome p{font-size:9px;line-height:1.4;color:#d9e7ea;margin-bottom:6px}
.hero-welcome span{font-size:8px;color:var(--tan)}
.hero-dots{position:absolute;right:12px;bottom:10px;display:flex;gap:3px}
.hero-dots i{width:14px;height:10px;background:rgba(0,0,0,.45)}

/* services */
.services{top:492px;text-align:center}
.section-title{font-size:20px;font-weight:600;color:#555;letter-spacing:.5px}
.rule{width:40px;height:2px;background:var(--tan);margin:6px auto 10px}
.services-intro{font-size:9px;line-height:1.5;color:var(--muted);width:600px;margin:0 auto}
.service-list{display:flex;justify-content:space-between;margin-top:24px;padding:0 20px}
.service{width:210px}
.service-icon{width:74px;height:74px;border-radius:50%;background:var(--teal);margin:0 auto 10px;display:flex;align-items:center;justify-content:center}
.service-icon svg{width:38px;height:38px}
.service h3{font-size:11px;font-weight:700;color:var(--teal);margin-bottom:5px}
.service p{font-size:8.5px;line-height:1.5;color:var(--muted)}

/* columns */
.columns{top:775px;display:flex;justify-content:space-between}
.col{width:222px}
.col-kicker{font-size:14px;color:#777;line-height:1}
.col-title{font-size:19px;font-weight:700;color:var(--teal);line-height:1.15;margin-bottom:8px}
.col-text{font-size:8.5px;line-height:1.55;color:var(--muted);margin-bottom:8px}
.col-photo{height:112px;margin-bottom:8px}
.photo-works{background:linear-gradient(135deg,#3a2a1c,#c2651e 55%,#2a2420)}
.photo-industrial{background:linear-gradient(135deg,#c9d3dc,#e0b23a 50%,#5a6a78)}
.btn{display:inline-block;background:var(--teal-dark);color:#fff;font-size:8px;font-weight:700;padding:6px 10px;letter-spacing:.4px}

/* footer */
.footer{position:absolute;left:0;top:1055px;width:880px;height:145px;background:var(--footer);text-align:center}
.social{display:flex;justify-content:center;gap:12px;padding-top:18px}
.social i{width:30px;height:30px;border-radius:50%;border:1px solid #777;background:#3a3a3a}
.footer-nav{display:flex;justify-content:center;gap:28px;margin-top:26px;padding-top:12px;border-top:1px solid #3d3d3d;width:734px;margin-left:73px}
.footer-nav a{font-size:8px;color:var(--footer-text);text-decoration:none}
.copyright{font-size:7.5px;color:#777;margin-top:12px}
</style>
</head>
<body>

<header>
  <div class="brand"><span class="brand-mark"></span><span class="brand-name">Velmoran Partners</span></div>
  <div class="search">Search <svg viewBox="0 0 12 12"><circle cx="5" cy="5" r="3.5" fill="none" stroke="#999" stroke-width="1.4"/><line x1="7.6" y1="7.6" x2="11" y2="11" stroke="#999" stroke-width="1.4"/></svg></div>
</header>

<nav class="wrap nav">
  <a class="active">HOME</a><a>VELMORAN</a><a>STRATEGY</a><a>TEAM</a><a>PORTFOLIO</a><a>PUBLICATIONS</a><a>INVESTORS</a><a>CONTACT US</a>
</nav>

<section class="wrap hero" role="img" aria-label="Photo of business people climbing a rising red growth arrow in front of a city skyline">
  <div class="hero-welcome">
    <h1>WELCOME TO VELMORAN PARTNERS</h1>
    <p>Your Trusted Partners to Achieve Special Situations and Expand to Growing Markets</p>
    <span>Read More »</span>
  </div>
  <div class="hero-dots"><i></i><i></i></div>
</section>

<section class="wrap services">
  <h2 class="section-title">OUR SERVICES</h2>
  <div class="rule"></div>
  <p class="services-intro">We partner with European industrial companies and help them build a lasting presence in India. Our team in Europe and India works side by side with owners, managers and investors to unlock new growth.</p>
  <div class="service-list">
    <div class="service">
      <div class="service-icon"><svg viewBox="0 0 40 40"><circle cx="20" cy="20" r="15" fill="none" stroke="#fff" stroke-width="2.5"/><circle cx="20" cy="20" r="9" fill="none" stroke="#fff" stroke-width="2.5"/><circle cx="20" cy="20" r="3.5" fill="#fff"/></svg></div>
      <h3>TARGET COMPANIES</h3>
      <p>We take stakes in mid-sized manufacturers with strong products and guide their entry into the Indian market.</p>
    </div>
    <div class="service">
      <div class="service-icon"><svg viewBox="0 0 40 40"><path d="M5 34V20l8 5v-5l8 5v-5l8 5V6h5v28z" fill="#fff"/></svg></div>
      <h3>TARGET INDUSTRIES</h3>
      <p>Machinery, components, automotive and engineering firms that can scale production and sales across India.</p>
    </div>
    <div class="service">
      <div class="service-icon"><svg viewBox="0 0 40 40"><circle cx="20" cy="20" r="14" fill="none" stroke="#fff" stroke-width="2.5"/><ellipse cx="20" cy="20" rx="6" ry="14" fill="none" stroke="#fff" stroke-width="2"/><line x1="6" y1="20" x2="34" y2="20" stroke="#fff" stroke-width="2"/></svg></div>
      <h3>WHY INDIA</h3>
      <p>A fast growing economy, a skilled workforce and rising demand make India the natural next step for growth.</p>
    </div>
  </div>
</section>

<section class="wrap columns">
  <article class="col">
    <div class="col-kicker">ABOUT</div>
    <h2 class="col-title">OUR COMPANY!</h2>
    <p class="col-text">We are a European and Indian investment firm with offices in Barcelona, Zurich, Amsterdam and Bangalore. We bring capital, experience and local knowledge to companies ready for the next stage.</p>
    <p class="col-text">Our partners have built and run industrial businesses on both continents, and we use that network to open doors for our portfolio.</p>
    <a class="btn">READ MORE</a>
  </article>
  <article class="col">
    <div class="col-kicker">EUROPEAN</div>
    <h2 class="col-title">MANUFACTURING</h2>
    <div class="col-photo photo-works" role="img" aria-label="Photo of sparks flying from metal work in a factory"></div>
    <p class="col-text">European craftsmanship and engineering quality, ready to be taken to new customers and new plants.</p>
    <a class="btn">READ MORE</a>
  </article>
  <article class="col">
    <div class="col-kicker">Companies</div>
    <h2 class="col-title">INDUSTRIAL</h2>
    <div class="col-photo photo-industrial" role="img" aria-label="Photo of an engineer in a hard hat at an industrial site"></div>
    <p class="col-text">Hands-on support for industrial companies setting up sourcing, production and sales in India.</p>
    <a class="btn">READ MORE</a>
  </article>
</section>

<footer class="footer">
  <div class="social"><i></i><i></i><i></i><i></i></div>
  <div class="footer-nav">
    <a>HOME</a><a>VELMORAN</a><a>STRATEGY</a><a>TEAM</a><a>PORTFOLIO</a><a>PUBLICATIONS</a><a>INVESTORS</a><a>CONTACT US</a>
  </div>
  <p class="copyright">© Copyright 2014 Velmoran Partners. All Rights Reserved.</p>
</footer>

</body>
</html>
```